Business card for a Exhibition booth fabrication company

Hi. My company would like to change our corporate name card. We are an events and Exhibition stand builder company. We would like our corporate name card to resonate what we do. I need someone to create something unique that relates to the industry that I am in. The graphic designer should be creative to incorporate the elements of my industry and try to blend in well in the design of the card. Our aim is to ensure that we are unique and our card can look different from our competitors.
Updates

The decision maker was very busy and didnt had time to make this decision

Target Market(s)

Marketing and events manager from all companies

Contact Information for Business Card

The business card should have the following details:
Name
Job Title
Email
Website

Colors

Designer to choose colors to be used in the design.

Requirements
Must have
• The card must be look something that is relevant to the service that I am providing. My website is: www.velmora-buildworks.example
• You can see my website to get more information on what service that I am doing
Nice to have
• On the back of my card, I would like to have a globe image with the incorporation of my company logo. This is to indicate that my services can be done in any part of the world.

```html
<!DOCTYPE html>
<html lang="en">
<head>
<meta charset="utf-8">
<title>Velmora Buildworks – Business Card</title>
<link rel="stylesheet" href="https://fonts.googleapis.com/css2?family=Montserrat:wght@600&family=Open+Sans:wght@400;600&family=Noto+Serif:wght@700&display=swap">
<style>
  :root {
    --bg: #3a3f47;
    --paper: #ffffff;
    --red: #e3222b;
    --deep-red: #7f0d10;
    --charcoal: #3b3a3c;
    --ink: #2f2f33;
    --map-light: #e6e6e6;
    --map-mid: #c4c4c4;
  }
  * { margin: 0; padding: 0; box-sizing: border-box; }
  html, body { width: 1200px; height: 1200px; overflow: hidden; background: var(--bg); }
  .canvas { position: relative; width: 1200px; height: 1200px; }

  .card {
    position: absolute;
    left: 150px;
    width: 900px;
    height: 514px;
    background: var(--paper);
    overflow: hidden;
    box-shadow: 0 10px 30px rgba(0,0,0,.35);
  }
  .card--front { top: 50px; }
  .card--back { top: 636px; }

  /* Front */
  .brand {
    position: absolute;
    left: 60px;
    top: 44px;
    display: flex;
    align-items: center;
    gap: 12px;
    font-family: "Montserrat", sans-serif;
    font-weight: 600;
    font-size: 20px;
    letter-spacing: 2px;
    color: var(--ink);
  }
  .brand__dot { width: 24px; height: 24px; border-radius: 50%; background: var(--red); }

  .person { position: absolute; left: 60px; top: 100px; }
  .person__name {
    font-family: "Open Sans", sans-serif;
    font-weight: 600;
    font-size: 40px;
    color: var(--ink);
    line-height: 1.1;
  }
  .person__first { color: var(--red); }
  .person__title {
    font-family: "Noto Serif", serif;
    font-weight: 700;
    font-size: 22px;
    color: var(--ink);
    margin-top: 2px;
  }
  .person__rule { width: 380px; height: 2px; background: var(--red); margin-top: 12px; }

  .contacts {
    position: absolute;
    left: 60px;
    top: 218px;
    list-style: none;
    font-family: "Open Sans", sans-serif;
    font-size: 22px;
    color: var(--ink);
  }
  .contacts li { display: flex; align-items: center; gap: 12px; height: 32px; }
  .contacts svg { width: 20px; height: 20px; flex: none; }

  .strip { position: absolute; top: 306px; height: 62px; }
  .strip--charcoal { left: 0; width: 210px; background: var(--charcoal); }
  .strip--deep-red { left: 224px; width: 136px; background: var(--deep-red); }
  .strip--red { left: 374px; width: 526px; background: var(--red); }

  .feature-mark {
    position: absolute;
    right: 40px;
    top: 396px;
    display: flex;
    align-items: center;
    gap: 22px;
    font-family: "Montserrat", sans-serif;
    font-weight: 600;
    font-size: 46px;
    letter-spacing: 3px;
    color: var(--red);
    white-space: nowrap;
  }
  .feature-mark__dot { width: 90px; height: 90px; border-radius: 50%; background: var(--red); flex: none; }

  /* Back */
  .world-map {
    position: absolute;
    left: 200px;
    top: 70px;
    width: 620px;
    height: 380px;
    border-radius: 45%;
    background: radial-gradient(ellipse at 50% 45%, var(--map-mid) 0%, var(--map-light) 55%, rgba(255,255,255,0) 72%);
  }
  .back-brand {
    position: absolute;
    left: 0; right: 0;
    top: 232px;
    display: flex;
    justify-content: center;
    align-items: center;
    gap: 16px;
    font-family: "Montserrat", sans-serif;
    font-weight: 600;
    font-size: 38px;
    letter-spacing: 4px;
    color: var(--ink);
  }
  .back-brand__dot { width: 36px; height: 36px; border-radius: 50%; background: var(--red); }
</style>
</head>
<body>
<div class="canvas">

  <section class="card card--front">
    <div class="brand"><span class="brand__dot"></span>VELMORA BUILDWORKS</div>

    <div class="person">
      <h1 class="person__name"><span class="person__first">ARLEN</span> VANCE</h1>
      <p class="person__title">Director</p>
      <div class="person__rule"></div>
    </div>

    <ul class="contacts">
      <li>
        <svg viewBox="0 0 20 20" aria-hidden="true">
          <rect x="0" y="2" width="20" height="16" rx="2" fill="#e3222b"/>
          <path d="M3 6 L10 11 L17 6" stroke="#fff" stroke-width="2" fill="none"/>
        </svg>
        username@velmora-buildworks.example
      </li>
      <li>
        <svg viewBox="0 0 20 20" aria-hidden="true">
          <circle cx="10" cy="10" r="10" fill="#e3222b"/>
          <g stroke="#fff" stroke-width="1.3" fill="none">
            <circle cx="10" cy="10" r="6.5"/>
            <ellipse cx="10" cy="10" rx="3" ry="6.5"/>
            <line x1="3.5" y1="10" x2="16.5" y2="10"/>
          </g>
        </svg>
        www.velmora-buildworks.example
      </li>
    </ul>

    <div class="strip strip--charcoal"></div>
    <div class="strip strip--deep-red"></div>
    <div class="strip strip--red"></div>

    <div class="feature-mark"><span class="feature-mark__dot"></span>VELMORA BUILDWORKS</div>
  </section>

  <section class="card card--back">
    <div class="world-map" role="img" aria-label="Soft grey world map showing global reach"></div>
    <div class="back-brand"><span class="back-brand__dot"></span>VELMORA BUILDWORKS</div>
  </section>

</div>
</body>
</html>
```